Flyer for an online formula one racing league

Hello.

I am looking for the perfect one page facebook/instagram style flyer for an online formula one racing league. The racing league is called 'VOLTA RACING LEAGUE'.

Information that MUST be on the new flyer is already on the old flyer I have uploaded here. In addition to including: The Volta racing league 'V' I have uploaded AND the text: 'Very popular, clean and competitive racing league, running for its 4th season. Why not join with a friend? Race times, Mondays, Tuesdays and Wednesdays each at 8pm UK TIME Message below for any questions. (Spacing of information is not important, however all the information in regards to the racing I have just mentioned MUST BE on the flyer, this includes info from old pic, logo and the other info I just mentioned).

It would be beneficial to have lots of dark blue on the flyer and the new flyer to be a lot different to the original flyer I uploaded, but this is not essential.

I apologise if I did not explain very well, any questions, please message me.

The best flyer should look the most attractive to someone that might be interested in joining an online formula one racing league.

I used this website before to create the perfect logo for my Sunday League team last year, and I was very impressed. I look forward to seeing your submissions.

Target Market(s)

No specific target, more something that may attract someone into joining a formula one online racing league

Industry/Entity Type

e sports/formula one

Colors
0054AA
0677BA
7BADD7
CADEEF
E8F1F8

Requirements
Must have
• Read product description please
Should not have
• Ignoring product description!

```html
<!DOCTYPE html>
<html lang="en">
<head>
<meta charset="utf-8">
<title>Volta Racing League – Join Us</title>
<link rel="stylesheet" href="https://fonts.googleapis.com/css2?family=Russo+One&family=Oswald:wght@500;600&display=swap">
<style>
  :root {
    --navy: #0b3b78;
    --navy-soft: #16488a;
    --badge: #0d1a34;
    --pink: #f0207c;
    --electric: #2434e6;
    --yellow: #f3f21c;
    --white: #ffffff;
  }
  html, body {
    margin: 0;
    padding: 0;
    width: 1200px;
    height: 628px;
    overflow: hidden;
    background: var(--navy);
  }
  .flyer {
    position: relative;
    width: 1200px;
    height: 628px;
    overflow: hidden;
    background: var(--navy);
    font-family: "Oswald", "Arial Narrow", sans-serif;
    color: var(--white);
    text-align: center;
  }
  .stripes {
    position: absolute;
    inset: 0;
  }
  .badge {
    position: absolute;
    top: 22px;
    width: 106px;
    height: 106px;
    border-radius: 50%;
    background: var(--badge);
    display: flex;
    align-items: center;
    justify-content: center;
    font-family: "Oswald", "Arial Narrow", sans-serif;
    font-weight: 600;
    font-size: 58px;
    color: var(--white);
  }
  .badge--left { left: 37px; }
  .badge--right { right: 37px; }
  .watermark-disc {
    position: absolute;
    left: 330px;
    top: 60px;
    width: 540px;
    height: 540px;
    border-radius: 50%;
    background: var(--navy-soft);
    opacity: 0.55;
  }
  .line {
    position: absolute;
    left: 0;
    right: 0;
    margin: 0;
    text-shadow: 2px 3px 3px rgba(0, 0, 0, 0.6);
  }
  .title {
    top: 28px;
    font-family: "Russo One", "Arial Black", sans-serif;
    font-style: italic;
    font-weight: 400;
    font-size: 64px;
    color: var(--yellow);
    letter-spacing: 1px;
  }
  .pitch {
    font-variant: small-caps;
    font-weight: 500;
    font-size: 50px;
    line-height: 1;
  }
  .pitch--one { top: 182px; }
  .pitch--two { top: 232px; }
  .invite {
    top: 296px;
    font-variant: small-caps;
    font-weight: 500;
    font-size: 62px;
    line-height: 1;
  }
  .label {
    top: 420px;
    font-size: 24px;
    font-weight: 500;
    letter-spacing: 2px;
  }
  .days {
    top: 448px;
    font-size: 44px;
    font-weight: 500;
    color: var(--yellow);
    letter-spacing: 5px;
  }
  .time {
    top: 508px;
    font-size: 24px;
    font-weight: 500;
    color: var(--yellow);
    letter-spacing: 2px;
  }
  .contact {
    top: 574px;
    font-size: 21px;
    font-weight: 500;
    letter-spacing: 3px;
  }
</style>
</head>
<body>
<main class="flyer">
  <svg class="stripes" width="1200" height="628" viewBox="0 0 1200 628" aria-hidden="true">
    <polygon points="0,190 0,228 310,0 270,0" fill="var(--pink)"/>
    <polygon points="0,240 0,278 380,0 340,0" fill="var(--electric)"/>
    <polygon points="905,628 945,628 1200,378 1200,340" fill="var(--pink)"/>
    <polygon points="965,628 1005,628 1200,436 1200,398" fill="var(--electric)"/>
  </svg>

  <div class="watermark-disc" aria-hidden="true"></div>

  <div class="badge badge--left">V</div>
  <div class="badge badge--right">V</div>

  <h1 class="line title">VOLTA RACING LEAGUE</h1>

  <p class="line pitch pitch--one">Very popular, clean and competitive racing league,</p>
  <p class="line pitch pitch--two">running for its 4th season.</p>
  <p class="line invite">Why not join with a friend?</p>

  <p class="line label">RACE TIMES:</p>
  <p class="line days">MONDAYS, TUESDAYS AND WEDNESDAYS</p>
  <p class="line time">8PM UK TIME</p>

  <p class="line contact">MESSAGE BELOW FOR ANY QUESTIONS</p>
</main>
</body>
</html>
```